Ironbark Shift Workforce

We are a underground coal mining labour hire company, needing a website that links into our online payroll (www.wagetrackly.com.au) and also need to have job applications page that is a preform with drop down menu,s with answers or check boxes. We would also need a 3 tier administration access for access to different files.
We are looking for an ongoing relationship with future app integration

Reason: There are a few more designs to come and I'm out at the mine for another week

Industry/Entity Type

Coal Mining

```html
<!DOCTYPE html>
<html lang="en">
<head>
<meta charset="utf-8">
<title>ShiftCoal — Ironbark Shift Workforce</title>
<link rel="stylesheet" href="https://fonts.googleapis.com/css2?family=Lato:wght@400;700;900&family=Montserrat:wght@400;500;600&family=Oswald:wght@600&display=swap">
<style>
  :root {
    --orange: #f08a12;
    --black: #000;
    --ink: #1e1e1e;
    --grey-text: #555;
    --soft-grey: #999;
    --rule: #d9d9d9;
    --strip: #ebebeb;
    --white: #fff;
  }
  * { box-sizing: border-box; margin: 0; padding: 0; }
  html, body { width: 1099px; height: 1200px; overflow: hidden; background: var(--white); }
  body { position: relative; font-family: "Lato", sans-serif; color: var(--ink); }

  .site-header { position: absolute; left: 0; top: 0; width: 1099px; height: 132px; background: var(--black); }
  .brand { position: absolute; left: 133px; top: 0; width: 150px; height: 128px; background: #111;
    display: flex; flex-direction: column; align-items: center; justify-content: center; gap: 8px; }
  .brand-dot { width: 34px; height: 34px; border-radius: 50%; background: var(--orange); }
  .brand-name { font-weight: 700; font-size: 13px; color: var(--orange); text-align: center; line-height: 1.2; }

  .login { position: absolute; top: 20px; left: 556px; display: flex; gap: 6px; }
  .login-field { width: 165px; height: 22px; background: var(--white); border: 1px solid #ccc; border-radius: 2px;
    font-size: 8px; color: #777; padding: 6px 10px; }
  .login-btn { width: 52px; height: 22px; background: var(--orange); color: var(--white); font-size: 10px; font-weight: 700;
    display: flex; align-items: center; justify-content: center; border-radius: 2px; }

  .phone { position: absolute; right: 152px; top: 58px; display: flex; align-items: center; gap: 5px;
    font-family: "Montserrat", sans-serif; font-weight: 600; font-size: 21px; color: var(--white); }
  .main-nav { position: absolute; right: 152px; top: 105px; display: flex; font-size: 12px; font-weight: 700; color: var(--white); }
  .main-nav span { padding: 0 10px; border-left: 1px solid var(--white); line-height: 12px; }
  .main-nav span:first-child { border-left: 0; }
  .main-nav span:last-child { padding-right: 0; }

  .hero { position: absolute; left: 0; top: 132px; width: 1099px; height: 413px;
    background:
      radial-gradient(ellipse 260px 200px at 180px 100px, rgba(200,200,200,.55), transparent 70%),
      radial-gradient(ellipse 220px 150px at 560px 230px, rgba(190,190,190,.45), transparent 70%),
      radial-gradient(ellipse 200px 160px at 430px 330px, rgba(10,10,10,.75), transparent 70%),
      radial-gradient(ellipse 170px 150px at 140px 330px, rgba(15,15,15,.7), transparent 70%),
      radial-gradient(ellipse 300px 380px at 900px 180px, rgba(15,15,15,.8), transparent 70%),
      linear-gradient(180deg, #8a8a8a 0%, #6a6a6a 55%, #8c8c8c 85%, #5a5a5a 100%); }
  .hero-title { position: absolute; right: 679px; top: 88px; text-align: right; color: var(--white);
    font-family: "Montserrat", sans-serif; font-weight: 500; font-size: 35px; line-height: 38.5px; }
  .hero-text { position: absolute; right: 673px; top: 209px; text-align: right; font-size: 13.6px; line-height: 20px; color: #eee; white-space: nowrap; }
  .slider-dots { position: absolute; left: 216px; top: 312px; display: flex; gap: 3px; }
  .slider-dots i { width: 10px; height: 10px; border-radius: 50%; background: var(--white); }
  .slider-dots i:first-child { background: var(--orange); }
  .hero-cta { position: absolute; left: 302px; top: 301px; width: 119px; height: 27px; background: var(--orange);
    border-radius: 3px; color: var(--white); font-family: "Montserrat", sans-serif; font-weight: 600; font-size: 12px;
    display: flex; align-items: center; justify-content: center; box-shadow: 0 1px 3px rgba(0,0,0,.5); }

  .service { position: absolute; top: 593px; width: 280px; }
  .service-banner { position: relative; height: 60px; }
  .service-art { position: absolute; left: 0; top: 2px; width: 56px; height: 56px; border-radius: 50%; }
  .service-band { position: absolute; left: 40px; top: 16px; right: 0; height: 30px;
    background: linear-gradient(90deg, #111 70%, var(--orange) 100%); }
  .service-title { position: absolute; left: 70px; top: 17px; font-family: "Oswald", sans-serif; font-weight: 600; font-size: 20px; color: var(--orange); letter-spacing: .3px; }
  .service-text { margin: 14px 0 0 68px; font-size: 11.5px; line-height: 15.5px; color: var(--ink); }
  .read-more { margin: 9px 0 0 68px; width: 81px; height: 22px; background: var(--ink); color: var(--white);
    font-size: 8.5px; font-weight: 700; display: flex; align-items: center; justify-content: center; }

  .divider { position: absolute; left: 155px; top: 792px; width: 795px; height: 1px; background: #e5e5e5; }

  .welcome-title { position: absolute; left: 157px; top: 827px; font-family: "Montserrat", sans-serif; font-size: 30px; font-weight: 400; color: var(--ink); letter-spacing: -.5px; }
  .welcome-title b { font-weight: 600; }
  .welcome-title .accent { color: var(--orange); font-weight: 600; }
  .welcome-text { position: absolute; left: 158px; top: 877px; width: 495px; font-size: 11.4px; line-height: 16.6px; color: var(--grey-text); }
  .pdf-art { position: absolute; left: 155px; top: 1008px; width: 57px; height: 57px; background: linear-gradient(180deg, #c62828 0 28%, #f2f2f2 28%); border-radius: 2px; }
  .download-bar { position: absolute; left: 212px; top: 1024px; width: 388px; height: 33px; background: var(--ink); border-radius: 2px;
    color: var(--white); font-family: "Montserrat", sans-serif; font-size: 11.6px; white-space: nowrap;
    display: flex; align-items: center; padding-left: 18px; }

  .news { position: absolute; left: 740px; top: 828px; width: 204px; }
  .news-heading { font-family: "Montserrat", sans-serif; font-weight: 600; font-size: 21px; color: var(--ink); padding-bottom: 4px; border-bottom: 1px solid var(--rule); }
  .news-item { display: flex; gap: 8px; padding: 11px 0 10px; border-bottom: 1px solid var(--rule); height: 65px; }
  .news-item:last-child { border-bottom: 0; }
  .news-date { position: relative; width: 52px; flex: none; }
  .news-date .month { position: absolute; left: 0; top: 34px; font-size: 8.5px; color: var(--orange); }
  .news-date .year { position: absolute; left: 33px; top: 28px; font-size: 9px; color: var(--orange); transform: rotate(-90deg); transform-origin: left top; }
  .news-date::after { content: ""; position: absolute; left: 50px; top: 0; width: 1px; height: 42px; background: var(--rule); }
  .news-body h4 { font-size: 10px; font-weight: 700; color: var(--ink); }
  .news-body p { font-size: 8.5px; line-height: 11.5px; color: var(--soft-grey); margin-top: 2px; }

  .partners { position: absolute; left: 0; top: 1088px; width: 1099px; height: 64px; background: var(--strip); }
  .partner { position: absolute; top: 22px; height: 20px; background: #c4c4c4; border-radius: 2px; }

  .site-footer { position: absolute; left: 0; top: 1152px; width: 1099px; height: 48px; background: var(--orange); color: var(--white); }
  .copyright { position: absolute; left: 152px; top: 16px; font-family: "Montserrat", sans-serif; font-size: 13px; }
  .follow { position: absolute; right: 152px; top: 12px; display: flex; align-items: center; gap: 5px; font-family: "Montserrat", sans-serif; font-weight: 600; font-size: 15px; }
  .follow i { width: 23px; height: 23px; border-radius: 50%; background: var(--white); }
  .follow span { margin-right: 3px; }
</style>
</head>
<body>
  <header class="site-header">
    <div class="brand">
      <div class="brand-dot"></div>
      <div class="brand-name">Ironbark Shift<br>Workforce</div>
    </div>
    <div class="login">
      <div class="login-field">User Name</div>
      <div class="login-field">Password</div>
      <div class="login-btn">Login</div>
    </div>
    <div class="phone">
      <svg width="29" height="29" viewBox="0 0 30 30" aria-hidden="true">
        <circle cx="15" cy="15" r="13" fill="none" stroke="#fff" stroke-width="2.2"/>
        <path d="M10.5 8.5l3 3-1.6 1.8c.8 1.8 2.2 3.3 4 4.1l1.8-1.6 3 3-2 2c-4.8-.6-9.6-5.4-10.2-10.3z" fill="#fff"/>
      </svg>
      +61 (0)2 5550 1847
    </div>
    <nav class="main-nav">
      <span>Home</span><span>Products</span><span>Services</span><span>About</span><span>News</span><span>Careers</span><span>Contact</span>
    </nav>
  </header>

  <section class="hero" role="img" aria-label="Black and white photo of a wheel loader and haul truck on a mine site">
    <h1 class="hero-title">Flexible<br>Resourceful<br>Reliable</h1>
    <p class="hero-text">Lorem ipsum dolor sit amet, consectetuer<br>adipiscing elit, sed diam nonummy nibh<br>euismod tincidunt ut laoreet dolore magna<br>aliquam erat volutpat. Ut wisi enim ad minim.</p>
    <div class="slider-dots"><i></i><i></i><i></i><i></i><i></i><i></i></div>
    <div class="hero-cta">WORK WITH US</div>
  </section>

  <article class="service" style="left:140px">
    <div class="service-banner">
      <div class="service-band"></div>
      <div class="service-art" role="img" aria-label="Traffic cone illustration" style="background:linear-gradient(180deg,#f7931e,#e05a00)"></div>
      <div class="service-title">UNDERGROUND</div>
    </div>
    <p class="service-text">Lorem Ipsum Dolor Sit Amet,<br>Consectetuer Adipiscing<br>Nonummy Nibh. ....</p>
    <div class="read-more">Read More &gt;&gt;</div>
  </article>

  <article class="service" style="left:453px">
    <div class="service-banner">
      <div class="service-band"></div>
      <div class="service-art" role="img" aria-label="Blue gear illustration" style="background:radial-gradient(circle,#2f6f9e,#123a5a)"></div>
      <div class="service-title">MAINTINANCE</div>
    </div>
    <p class="service-text">Lorem Ipsum Dolor Sit Amet,<br>Consectetuer Adipiscing<br>Nonummy Nibh. ....</p>
    <div class="read-more">Read More &gt;&gt;</div>
  </article>

  <article class="service" style="left:731px">
    <div class="service-banner">
      <div class="service-band"></div>
      <div class="service-art" role="img" aria-label="Orange hard hat illustration" style="background:linear-gradient(180deg,#f9a53a,#d9620a)"></div>
      <div class="service-title">MAN POWER</div>
    </div>
    <p class="service-text">Lorem Ipsum Dolor Sit Amet,<br>Consectetuer Adipiscing<br>Nonummy Nibh. ....</p>
    <div class="read-more">Read More &gt;&gt;</div>
  </article>

  <div class="divider"></div>

  <h2 class="welcome-title">Wellcome To <b>Shift</b><span class="accent">Coal</span></h2>
  <p class="welcome-text">Lorem ipsum dolor sit amet, consectetuer adipiscing elit, sed diam nonummy nibh euismod tincidunt ut laoreet dolore magna aliquam erat volutpat. Ut wisi enim ad minim.Lorem ipsum dolor sit amet, consectetuer adipiscing elit, sed diam nonummy nibh euismod tincidunt ut laoreet dolore magna aliquam erat volutpat. Ut wisi enim ad minim.Lorem ipsum dolor sit amet, consectetuer adipiscing elit, sed diam nonummy nibh euismod tincidunt ut laoreet dolore magna aliquam erat volutpat. Ut wisi enim ad minim.Lorem ipsum dolor sit amet, consectetuer adipiscing elit, sed diam nonummy nibh euismod tincidunt ut laoreet dolore magna aliquam .</p>
  <div class="pdf-art" role="img" aria-label="PDF document icon"></div>
  <div class="download-bar">Dowlaod Information Of The Products And The Application</div>

  <aside class="news">
    <h3 class="news-heading">LATEST NEWS</h3>
    <div class="news-item">
      <div class="news-date">
        <svg width="30" height="30" viewBox="0 0 30 30" aria-hidden="true"><rect x="1.5" y="4" width="27" height="24" fill="#fff" stroke="#1e1e1e" stroke-width="3"/><rect x="7" y="1" width="3" height="6" fill="#1e1e1e"/><rect x="20" y="1" width="3" height="6" fill="#1e1e1e"/><text x="15" y="25" text-anchor="middle" font-family="Lato, sans-serif" font-size="17" fill="#f08a12">2</text></svg>
        <span class="month">MARCH</span><span class="year">2013</span>
      </div>
      <div class="news-body"><h4>Lorem ipsum</h4><p>Lorem ipsum dolor sit amet, consectetuer adipiscing elit , sed diam nonummy nibh</p></div>
    </div>
    <div class="news-item">
      <div class="news-date">
        <svg width="30" height="30" viewBox="0 0 30 30" aria-hidden="true"><rect x="1.5" y="4" width="27" height="24" fill="#fff" stroke="#1e1e1e" stroke-width="3"/><rect x="7" y="1" width="3" height="6" fill="#1e1e1e"/><rect x="20" y="1" width="3" height="6" fill="#1e1e1e"/><text x="15" y="25" text-anchor="middle" font-family="Lato, sans-serif" font-size="17" fill="#f08a12">2</text></svg>
        <span class="month">MARCH</span><span class="year">2013</span>
      </div>
      <div class="news-body"><h4>Lorem ipsum</h4><p>Lorem ipsum dolor sit amet, consectetuer adipiscing elit , sed diam nonummy nibh</p></div>
    </div>
    <div class="news-item">
      <div class="news-date">
        <svg width="30" height="30" viewBox="0 0 30 30" aria-hidden="true"><rect x="1.5" y="4" width="27" height="24" fill="#fff" stroke="#1e1e1e" stroke-width="3"/><rect x="7" y="1" width="3" height="6" fill="#1e1e1e"/><rect x="20" y="1" width="3" height="6" fill="#1e1e1e"/><text x="15" y="25" text-anchor="middle" font-family="Lato, sans-serif" font-size="17" fill="#f08a12">2</text></svg>
        <span class="month">MARCH</span><span class="year">2013</span>
      </div>
      <div class="news-body"><h4>Lorem ipsum</h4><p>Lorem ipsum dolor sit amet, consectetuer adipiscing elit , sed diam nonummy nibh</p></div>
    </div>
  </aside>

  <section class="partners" aria-label="Partners">
    <div class="partner" style="left:156px;width:50px"></div>
    <div class="partner" style="left:270px;width:82px"></div>
    <div class="partner" style="left:414px;width:72px"></div>
    <div class="partner" style="left:549px;width:80px"></div>
    <div class="partner" style="left:691px;width:44px"></div>
    <div class="partner" style="left:797px;width:82px"></div>
  </section>

  <footer class="site-footer">
    <p class="copyright">Copyright 2014 SHIFTCOAL All Rights Reserved</p>
    <div class="follow"><span>FOLLOW US :</span><i></i><i></i><i></i></div>
  </footer>
</body>
</html>
```